Redesign Mivorly.com Front Landing Page To Give It The Wow Factor Keeping SEO and Page Load Speeds

We need to redesign the landing page of www.mivorly.com to give it the wow factor

It must have exactly the same content, page size (currently 5.04 KB) or (5,156 bytes) and speed of the current site and rank 100/100 with Trelvix.com tools as the page currently does.

This of course is subjective to content - in other words for an outstanding design - leeway will be given - THE WOW FACTOR IS CRITICAL.

THE PAGE MUST BE HTML5 COMPLIANT AND TOTALLY COMPLETE INCLUDING ANY SCRIPTS, CSS ETC, AND READY TO UPLOAD THE HTML PAGE AND CONTENT FOLDER TO THE SERVER WITH NO MODIFICATIONS REQUIRED.

SERVER IS CURRENTLY KORVANT 2008 HUBCORE R2 BUT WILL SHORTLY BE UPGRADED TO KORVANT 2012 HUBCORE R2 SERVER.

The current landing page loads faster that 96 % of the sites on the web according to Trelvix Tools and that is on our current cable line connection that we are using while site is in development.

So we are looking for a fully optimized page that gives a outstanding first impression and SEO optimized.

It must be fully responsive for all screen size and utilize full page design on larger screen sizes.

The logo will remain to be strictly CSS and there are to be no images used on landing page other than the category link pages, all images must be fully optimized yet sharp and crisp.

A CSS content slider may be used to replace the Javascript rotator currently used - example www.glidepanez.com - we do have a licence for that slider

The winner will also be asked to look at the main script page and given priority in a contest for that as well.

Target Market(s)

World Online Trading Advertising and Business Directory Community Members

Industry/Entity Type

Seo

Requirements
Must have
• A feel of community - must be simple and clean.
• HTML5 Compliant
• Fully SEO optimized but not keyword spammed
• Keep the same content and links as existing landing page
• Search must be fully working and same as current options
Nice to have
• A WOW factor CSS slider - not bloated
Should not have
• No flash or any content that would slow down the front landing page Load Times

```html
<!DOCTYPE html>
<html lang="en">
<head>
<meta charset="utf-8">
<title>Mivorly – Free Ads, Auctions, Buy, Sell, Trade, Wanted</title>
<link rel="stylesheet" href="https://fonts.googleapis.com/css2?family=Hind:wght@400;500;600&family=Open+Sans:wght@700&display=swap">
<style>
:root{
  --orange:#c93d0c;
  --orange-tab:#d9480f;
  --blue:#4aa6ec;
  --blue-dark:#2d8fd8;
  --sky:#6ab8f3;
  --ink:#333;
  --line:#dcdcdc;
  --topbar:#ededed;
  --footer:#e4e4e4;
  --white:#fff;
  --banner-light:#e9eef3;
  --banner-deep:#2a72bd;
}
*{box-sizing:border-box;margin:0;padding:0}
html,body{width:1200px;height:2375px;overflow:hidden}
body{font-family:"Hind",Arial,sans-serif;color:var(--ink);background:var(--white);position:relative}
a{color:inherit;text-decoration:none}

/* top bar */
.topbar{height:41px;background:var(--topbar);display:flex;align-items:center;justify-content:space-between;padding:0 74px 0 76px}
.logo{font-weight:600;font-size:27px;color:var(--orange);letter-spacing:-.3px}
.utility-nav{display:flex;gap:34px;font-size:12.5px;color:#444}

/* main nav row */
.navrow{height:56px;position:relative}
.main-nav{position:absolute;left:79px;top:18px;width:507px;height:38px;background:var(--orange-tab);
  clip-path:polygon(12px 0,100% 0,100% 100%,0 100%);display:flex;align-items:center;gap:27px;padding-left:26px;
  font-size:12px;color:var(--white);text-transform:uppercase}
.region-select{position:absolute;left:709px;top:18px;width:146px;height:38px;background:var(--blue);color:var(--white);
  font-size:12px;display:flex;align-items:center;justify-content:center;gap:10px}
.region-select svg{width:10px;height:7px}
.site-search{position:absolute;left:871px;top:18px;width:256px;height:38px;background:var(--blue);padding:6px 12px}
.site-search .field{background:var(--white);height:26px;display:flex;align-items:center;justify-content:space-between;padding:0 8px;
  font-size:12px;font-style:italic;color:#888}

/* hero */
.hero{position:absolute;top:97px;left:0;width:1200px;height:356px;
  background:linear-gradient(100deg,#8a5a38 0%,#b07a4c 22%,#9a6c4a 45%,#6c5446 70%,#8a6e58 100%);text-align:center}
.hero-title{position:absolute;top:120px;width:100%;font-family:"Open Sans",Arial,sans-serif;font-weight:700;font-size:32px;color:var(--white);letter-spacing:.5px}
.hero-sub{position:absolute;top:170px;left:250px;width:700px;font-size:26px;line-height:32px;font-weight:500;color:var(--sky);letter-spacing:.5px}
.dots{position:absolute;top:316px;left:571px;display:flex;gap:7px}
.dots span{width:12px;height:12px;border-radius:50%;background:var(--white)}
.dots span.active{background:var(--orange-tab)}

/* search panel */
.finder{position:absolute;left:74px;top:470px;width:1052px;height:184px;background:var(--blue);padding:22px 24px;color:var(--white)}
.finder h2{font-weight:400;font-size:21px;letter-spacing:.4px;text-transform:uppercase}
.finder-row{position:absolute;top:57px;left:24px;display:flex;align-items:center}
.keyword{width:521px;height:40px;background:var(--white);color:#777;font-size:12.5px;font-style:italic;padding:0 12px;display:flex;align-items:center}
.in-label{width:57px;text-align:center;font-size:13px}
.category-select{width:207px;height:40px;background:var(--white);color:#666;font-size:12.5px;font-style:italic;padding:0 12px;display:flex;align-items:center;justify-content:space-between}
.search-btn{margin-left:11px;width:208px;height:40px;background:var(--orange);font-size:14px;display:flex;align-items:center;justify-content:center;text-transform:uppercase}
.options{position:absolute;left:24px;top:116px;display:grid;grid-template-columns:152px 167px 198px 200px;row-gap:12px;font-size:12.5px}
.options label{display:flex;align-items:center;gap:8px}
.options i{width:14px;height:14px;border-radius:50%;background:var(--white);display:inline-block}

/* sponsor banner slot */
.sponsor-slot{position:absolute;left:264px;top:678px;width:672px;height:82px;border:1px solid #bbb;
  background:linear-gradient(90deg,var(--banner-light) 0 28%,var(--banner-deep) 28% 100%)}

.rule{position:absolute;left:74px;top:782px;width:1052px;height:1px;background:var(--line)}

/* sidebar */
.sidebar{position:absolute;left:74px;top:810px;width:243px;height:1204px;background:var(--blue)}
.sidebar h3{height:46px;background:var(--orange);color:var(--white);font-weight:400;font-size:16px;padding:14px 16px 0;text-transform:uppercase}
.sidebar ul{list-style:none;padding:6px 17px 0 14px}
.sidebar li{height:33.2px;border-bottom:1px dashed rgba(255,255,255,.45);color:var(--white);font-size:12.5px;display:flex;align-items:center;gap:6px;padding-top:4px}
.sidebar li::before{content:"»";font-size:12px}

/* categories */
.popular-title{position:absolute;left:340px;top:817px;font-size:22px;font-weight:400;color:var(--orange);text-transform:uppercase;letter-spacing:.3px}
.grid{position:absolute;left:342px;top:860px;display:grid;grid-template-columns:repeat(3,242px);column-gap:27px;row-gap:19px}
.card{height:215px;border:1px solid var(--line);padding:12px;text-align:center}
.card .photo{height:158px}
.card p{margin-top:17px;font-size:12px;color:var(--orange);text-transform:uppercase}

/* footer */
.footer{position:absolute;left:0;top:2284px;width:1200px;height:91px;background:var(--footer);display:flex;align-items:center;justify-content:space-between;padding:0 74px;font-size:12px;color:#444}
.connect{display:flex;align-items:center;gap:6px}
.connect span{margin-right:10px}
.connect i{width:30px;height:30px;border-radius:50%;background:var(--blue-dark);display:inline-block}
</style>
</head>
<body>

<header class="topbar">
  <a class="logo" href="#">Mivorly</a>
  <nav class="utility-nav">
    <a href="#">FEATURES</a><a href="#">MAP LISTINGS</a><a href="#">POST FREE AD</a><a href="#">POST FREE AUCTION</a><a href="#">STORES</a>
  </nav>
</header>

<div class="navrow">
  <nav class="main-nav">
    <a href="#">Home</a><a href="#">About Us</a><a href="#">Community</a><a href="#">Help</a><a href="#">Contact Us</a><a href="#">Site Map</a>
  </nav>
  <div class="region-select">SELECT REGIONS
    <svg viewBox="0 0 10 7"><path d="M0 0h10L5 7z" fill="#fff"/></svg>
  </div>
  <div class="site-search"><div class="field">Search...
    <svg width="12" height="12" viewBox="0 0 12 12"><circle cx="5" cy="5" r="3.6" fill="none" stroke="#333" stroke-width="1.6"/><path d="M7.6 7.6L11 11" stroke="#333" stroke-width="1.8"/></svg>
  </div></div>
</div>

<section class="hero" role="img" aria-label="Laptop screen showing an online auction listing for a house">
  <h1 class="hero-title">FREE ADS - AUCTIONS - BUY - SELL - TRADE - WANTED</h1>
  <p class="hero-sub">* GLOBAL * REGIONAL * LOCAL * AUCTION CLASSIFIED &amp; DIRECTORY LISTINGS</p>
  <div class="dots"><span class="active"></span><span></span><span></span></div>
</section>

<section class="finder">
  <h2>What are you looking for</h2>
  <div class="finder-row">
    <div class="keyword">Enter Keyword....</div>
    <div class="in-label">IN</div>
    <div class="category-select">All Categories
      <svg width="10" height="6" viewBox="0 0 10 6"><path d="M0 0h10L5 6z" fill="#999"/></svg>
    </div>
    <div class="search-btn">Search Now</div>
  </div>
  <div class="options">
    <label><i></i>Search Titles</label><label><i></i>Title &amp; Description</label><label><i></i>Match Whole Words</label><label><i></i>Partial Word Match</label>
    <label><i></i>Classifieds Only</label><label><i></i>Auctions Only</label><label><i></i>Auctions &amp; Classifieds</label><label><i></i>Buy Now Auctions</label>
  </div>
</section>

<aside class="sponsor-slot" role="img" aria-label="Sponsor advertisement banner"></aside>

<div class="rule"></div>

<nav class="sidebar">
  <h3>Browse Categories</h3>
  <ul>
    <li>Activities &amp; Events</li><li>Antiques &amp; Collectables</li><li>Automotive &amp; Vehicles</li><li>Aviation &amp; Planes</li>
    <li>Boats &amp; Watercraft</li><li>Business Directory</li><li>Business to Business</li><li>Charities &amp; Non Profits</li>
    <li>Clothing &amp; Accessories</li><li>Computing &amp; Networking</li><li>Construction &amp; Logging</li><li>Daily Deals &amp; Services</li>
    <li>Dining-Food &amp; Beverages</li><li>Education &amp; Training</li><li>Electronics &amp; Phones</li><li>Employment &amp; Careers</li>
    <li>Farming &amp; Agriculture</li><li>Heavy Trucks &amp; Trailers</li><li>Home &amp; Garden</li><li>Industrial Machinery</li>
    <li>Jewelry &amp; Watches</li><li>Motorsports &amp; Racing</li><li>Office &amp; Restaurant</li><li>Personal Services</li>
    <li>Photography &amp;Equipment</li><li>Public News &amp; Events</li><li>Real Estate &amp; Rentals</li><li>Resorts Tickets &amp; Travel</li>
    <li>Sporting Goods &amp; Act.</li><li>RV'S Trailers &amp; Access..</li><li>Tools Hand/Power</li><li>Wanted &amp; Barter/Free</li>
  </ul>
</nav>

<h2 class="popular-title">Browse our most popular categories</h2>
<main class="grid">
  <a class="card" href="#"><div class="photo" role="img" aria-label="Antique clock and wooden chest" style="background:linear-gradient(160deg,#3a1e12,#7a3a1c 55%,#2a150c)"></div><p>Antiques/Collectables</p></a>
  <a class="card" href="#"><div class="photo" role="img" aria-label="Dark compact car parked in a street" style="background:linear-gradient(180deg,#7d8a84,#4a4f4e 60%,#8a8a86)"></div><p>Automotive - Vehicles</p></a>
  <a class="card" href="#"><div class="photo" role="img" aria-label="Motor yacht cruising on blue water" style="background:linear-gradient(180deg,#2f5e8a,#1e4a78 50%,#3d7db0)"></div><p>Boats - Watercraft</p></a>
  <a class="card" href="#"><div class="photo" role="img" aria-label="Volunteers handing out donated blankets" style="background:linear-gradient(120deg,#4c6f98,#c9c2b6 55%,#7a5a46)"></div><p>Charities &amp; Non Profits</p></a>
  <a class="card" href="#"><div class="photo" role="img" aria-label="Business people reviewing documents together" style="background:linear-gradient(120deg,#dfe6ee,#2e4766 55%,#b9c6d4)"></div><p>Business to Business</p></a>
  <a class="card" href="#"><div class="photo" role="img" aria-label="Index card file with address cards" style="background:linear-gradient(160deg,#6d87a8,#e6e2d8 45%,#c8c2b4)"></div><p>Business Directory</p></a>
  <a class="card" href="#"><div class="photo" role="img" aria-label="Engineer beside a bulldozer at a construction site" style="background:linear-gradient(180deg,#c8ccd0,#9a9890 55%,#6a5e48)"></div><p>Construction - Logging</p></a>
  <a class="card" href="#"><div class="photo" role="img" aria-label="Daily deals website on a screen" style="background:linear-gradient(135deg,#3a3a3a,#5ea83a 50%,#d8e8c8)"></div><p>Daily Deals/Services</p></a>
  <a class="card" href="#"><div class="photo" role="img" aria-label="Group of business professionals standing together" style="background:linear-gradient(180deg,#e2e2e2,#3c3c44 60%,#24242a)"></div><p>Employment/Carrers</p></a>
  <a class="card" href="#"><div class="photo" role="img" aria-label="Semi truck with trailer on the road" style="background:linear-gradient(180deg,#5a7896,#b4c0cc 50%,#3a3a3a)"></div><p>Heavy Trucks - Trailers</p></a>
  <a class="card" href="#"><div class="photo" role="img" aria-label="Metal gears and cogs" style="background:linear-gradient(135deg,#2a3a6a,#7a8ab8 50%,#3a4a7a)"></div><p>Industrial - Equipment</p></a>
  <a class="card" href="#"><div class="photo" role="img" aria-label="Race car in the pit lane with crew" style="background:linear-gradient(160deg,#6a6a6a,#b82020 50%,#4a4a4a)"></div><p>Motorsports - Racing</p></a>
  <a class="card" href="#"><div class="photo" role="img" aria-label="Camper trailer parked on grass near hills" style="background:linear-gradient(180deg,#9ab4cc,#e8e8e4 45%,#5e8a3c)"></div><p>RV's Campers/Trailers</p></a>
  <a class="card" href="#"><div class="photo" role="img" aria-label="Assorted sports balls on black" style="background:radial-gradient(circle at 60% 55%,#c86a2a,#111 60%)"></div><p>Sports - Equip/Access..</p></a>
  <a class="card" href="#"><div class="photo" role="img" aria-label="Resort terrace with palms and loungers" style="background:linear-gradient(180deg,#3c84c8,#9ac0d8 45%,#4a5a40)"></div><p>Resort Travel/Lodging</p></a>
  <a class="card" href="#"><div class="photo" role="img" aria-label="Hand passing house keys in front of an apartment building" style="background:linear-gradient(160deg,#3a78c0,#c8ccd2 55%,#8a9aaa)"></div><p>Real Estate - Rentals</p></a>
  <a class="card" href="#"><div class="photo" role="img" aria-label="Hand tools laid out on a light surface" style="background:linear-gradient(135deg,#d8d8d8,#8a8a8a 50%,#c8a070)"></div><p>Tools Hand/Power</p></a>
  <a class="card" href="#"><div class="photo" role="img" aria-label="Combine harvester in a wheat field" style="background:linear-gradient(180deg,#4a8ad0,#a8c8e8 40%,#d8a840 60%,#b88a2a)"></div><p>Farming - Agriculture</p></a>
</main>

<footer class="footer">
  <p>Copyright © 2015.CompanyName.All Right Reserved</p>
  <div class="connect"><span>Connect Us:</span><i></i><i></i><i></i></div>
</footer>

</body>
</html>
```